UI Mockup For Online Scheduling Software

11.01.2018 - Brief Update:
The brief has not changed but the summary below as being added to aid designers.

- New file added "Updated 11.01.2018 - Individual Box" to clarify the sections. Specifically the primary tag section
- Improve on the current styling
- Consider changing the section layout to maximise the number of blocks displayed on screen (The sections dont not need to be stacked like the current version.
- The design is for the application running on a desktop PC with 16:9 screen aspect
- The design styling/layout should not look like the current version
- You may use the application to get an understanding of its workings at this link....https://tomsbrevik.lqnhosting.com.au/
- Think outside the box....use your creative flare and show me something different to the current app (style and layout)

There are already some good submissions so closer to the deadline I will increase the budget and award $$$ to 1st and 2nd. The winner will be chosen to directly work on the remaining aspects of this application (setting page, mobile design, dashboard etc). The next design project associated to this application will be 10 time bigger than this one.

Good Luck Designers

*************************************************************
Redesign the user interface to make more efficient use of the screen real estate.

The software works by adding (Drag & Drop) Project Blocks to a Date Section. Then tags are added (Drag & Drop) to the block section below the header, and then resources are added to the block section below the tags.
Each block has 4 main sections that are stacked vertically:

1. Header - Displays Title and Address
2. Tags - Displays tags, maximum of 6 tags
3. Resources - Displays resources, maximum of 10 resources, NOTE: this section can be hidded.
4. Footer - Display basic stats (eg. 3 Resources assigned)

It is critical that as many block (20-30) as possible for a single date can be visible on screen.

The following criteria must be considered when mocking up layout:
1. Font Type, size, colour and emphasis
2. Block Colour/Shading, borders ect
3. Section Layout within the block (stacking & Alignment)
4. Mock ups to show scaled layout of blocks in both the open state and Closed State.
5. Mock up to display a minimum of 20 blocks.
6. Create a variation of your design that adds a 5th section. This will display the first tag only:
1. Header - Always Visible
2. Primary Tag - Always Visible
3. Secondary Tags - Can be hidden
4. Resources - Can be Hidden
5. Footer - Can be Hidden

Please be creative with your design and layout. I like a clean, minimalist design.
At this stage CSS file will not be required but would be benificial

Target Market(s)

N/A

Industry/Entity Type

Software

Number of Pages Required

1 page

Font styles to use
Other font styles liked:
• Designers Choice

Colors

Designer to choose colors to be used in the design.

Requirements
Must have
• Variation to current layout and style
Should not have
• Same styling and layout as current design

```html
<!DOCTYPE html>
<html lang="en">
<head>
<meta charset="utf-8">
<title>Scheduler – Daily Board</title>
<link href="https://fonts.googleapis.com/css2?family=Roboto:wght@400;500;700&display=swap" rel="stylesheet">
<style>
:root{
  --topbar:#3a4047;
  --orange:#f7941d;
  --panel:#eeeeee;
  --white:#ffffff;
  --text:#333a40;
  --muted:#6b7075;
  --line:#d9d9d9;
  --teal:#5bc3a6;
  --mint:#4fd1b5;
  --pink:#ee2a5e;
  --blue:#3b8ded;
  --blue-dark:#2f7bd6;
  --tag-red:#e8417a;
  --ok:#35b34a;
  --badge-blue:#4a90e2;
  --badge-red:#ef3e5c;
  --badge-green:#3aae7c;
  --badge-orange:#f7941d;
  --btn:#dddddd;
}
*{box-sizing:border-box;margin:0;padding:0}
html,body{width:1200px;height:675px;overflow:hidden}
body{font-family:"Roboto",Arial,sans-serif;color:var(--text);background:var(--panel);position:relative}
svg{display:block}

/* top bar */
.topbar{position:absolute;left:0;top:0;width:1200px;height:52px;background:var(--topbar)}
.brand{position:absolute;left:14px;top:13px;font-size:22px;font-weight:700;color:var(--white);letter-spacing:.3px}
.brand span{color:var(--orange)}
.top-search{position:absolute;left:342px;top:10px;width:274px;height:32px;border-radius:16px;background:#4c535b;color:#a7adb3;font-size:14px;padding:8px 16px}
.top-search svg{position:absolute;right:16px;top:8px}
.bell{position:absolute;left:953px;top:18px}
.bell-dot{position:absolute;left:961px;top:15px;width:10px;height:10px;border-radius:50%;background:var(--pink);color:#fff;font-size:7px;text-align:center;line-height:10px}
.gear{position:absolute;left:1005px;top:18px}
.greeting{position:absolute;left:1064px;top:18px;font-size:14px;color:#c9cdd1}
.greeting b{color:var(--white);font-weight:400}
.avatar{position:absolute;left:1134px;top:10px;width:32px;height:32px;border-radius:50%;background:linear-gradient(135deg,#8a7a66,#c9b59a)}
.caret{position:absolute;left:1174px;top:22px}

/* main nav */
.mainnav{position:absolute;left:0;top:52px;width:157px;height:623px;background:var(--white)}
.nav-item{position:absolute;left:0;width:157px;font-size:14px;color:var(--text)}
.nav-item .ico{position:absolute;left:14px;top:0}
.nav-item .lbl{position:absolute;left:42px;top:1px}
.nav-item .chev{position:absolute;left:136px;top:5px}
.nav-active{background:var(--panel);height:69px;top:57px}
.nav-active .lbl{top:16px}
.nav-active .ico{top:15px}
.nav-active .chev{top:20px}
.nav-active .sub{position:absolute;left:42px;top:42px;font-size:12px;color:var(--orange)}

/* sub panel */
.subpanel{position:absolute;left:157px;top:52px;width:184px;height:623px;background:var(--panel)}
.show{height:42px;background:var(--orange);color:var(--white);font-size:18px;font-weight:500;text-align:center;line-height:42px}
.sub-item{position:absolute;left:0;width:184px;height:34px;font-size:14px;color:var(--text)}
.sub-item .arrow{position:absolute;left:12px;top:12px}
.sub-item .ico{position:absolute;left:28px;top:7px}
.sub-item .lbl{position:absolute;left:57px;top:9px}
.badge{position:absolute;left:161px;top:10px;min-width:15px;height:14px;padding:0 2px;font-size:9px;color:#fff;text-align:center;line-height:14px}
.sub-item.current{background:#e2e2e2;color:var(--orange)}
.tag-search{position:absolute;left:10px;top:221px;width:161px;height:30px;background:var(--white);border:1px solid #e4e4e4;font-size:12px;color:#9aa0a5;padding:8px 10px}
.group-title{position:absolute;left:9px;font-size:14px;color:var(--text)}
.chip{position:absolute;left:10px;width:161px;height:24px;background:#f4f4f4;border:1px solid #dcdcdc;box-shadow:0 1px 1px rgba(0,0,0,.08);font-size:11px;color:var(--text);padding:5px 0 0 32px}
.chip svg{position:absolute;left:10px;top:6px}
.scroll-track{position:absolute;left:336px;top:322px;width:2px;height:62px;background:#c9c9c9}
.collapse{position:absolute;left:64px;top:622px;width:29px;height:29px;border-radius:50%;background:#d4d4d4}
.collapse svg{position:absolute;left:10px;top:9px}

/* filter */
.filter{position:absolute;left:353px;top:62px;width:833px;height:81px;background:var(--white)}
.filter-title{position:absolute;left:13px;top:28px;font-size:20px;color:#5d6368}
.field{position:absolute;top:9px;height:27px;border:1px solid #dcdcdc;font-size:12px;color:#4d5358;padding:6px 9px}
.field svg{position:absolute;right:8px;top:6px}
.btn{position:absolute;top:44px;height:28px;font-size:12px;text-align:center;line-height:28px;color:#4d5358;background:var(--btn);border:1px solid #d0d0d0}
.btn.apply{background:var(--mint);color:#fff;border:none}
.btn.clear{background:var(--pink);color:#fff;border:none}

/* date bar */
.datebar{position:absolute;left:353px;top:154px;width:833px;height:32px;background:var(--teal);color:var(--white)}
.datebar .cal{position:absolute;left:10px;top:8px}
.datebar .day{position:absolute;left:38px;top:8px;font-size:14px;font-weight:500}
.datebar .comment{position:absolute;left:416px;top:10px;font-size:10.5px;font-weight:500}
.datebar .comment svg{display:inline-block;margin-left:6px;vertical-align:middle}
.datebar .stat{position:absolute;top:10px;font-size:10.5px;font-weight:500}

/* board */
.board{position:absolute;left:353px;top:186px;width:833px;height:475px;background:var(--white);padding:10px 9px 0 9px;display:grid;grid-template-columns:repeat(7,109px);column-gap:8.3px;row-gap:8.5px}
.block{height:145px;background:#fafafa;box-shadow:0 1px 3px rgba(0,0,0,.22);position:relative;font-size:7.6px;color:#444}
.block-head{height:22px;background:var(--blue);color:var(--white);padding:1px 3px;position:relative}
.block-head .title{font-size:9.6px;font-weight:500;line-height:11px;white-space:nowrap}
.block-head .addr{font-size:5.4px;line-height:7px;opacity:.95}
.block-head svg{position:absolute;right:4px;top:12px}
.tags{padding:4px 4px 0 4px}
.row{height:11.6px;line-height:11.6px;position:relative;padding-left:13px;white-space:nowrap}
.row svg{position:absolute;left:2px;top:3px}
.row .x{position:absolute;right:1px;top:0;color:var(--tag-red);font-size:7px}
.row.trade{color:var(--tag-red)}
.row.ok{color:var(--ok)}
.crew{margin:5px 4px 0 4px;height:42px;background:#efefef;border:1px solid #e2e2e2;padding:1px 0 0 0}
.crew .row{padding-left:19px}
.crew .row svg{left:5px}
.crew .row.lead{font-weight:700}
.foot{position:absolute;left:4px;bottom:3px;font-size:6.8px;color:#555}
</style>
</head>
<body>
<svg width="0" height="0" style="position:absolute">
  <defs>
    <symbol id="i-tag" viewBox="0 0 16 16"><path d="M1 2v5l8 8 6-6-8-8H2z" fill="currentColor"/><circle cx="4.5" cy="4.5" r="1.3" fill="#fff"/></symbol>
    <symbol id="i-tag-o" viewBox="0 0 16 16"><path d="M1.5 2.5v4.5l8 8 5.5-5.5-8-8H2.5z" fill="none" stroke="currentColor" stroke-width="1.5"/><circle cx="5" cy="5" r="1.2" fill="currentColor"/></symbol>
    <symbol id="i-gear" viewBox="0 0 16 16"><circle cx="8" cy="8" r="5" fill="none" stroke="currentColor" stroke-width="3" stroke-dasharray="2.4 1.5"/><circle cx="8" cy="8" r="2.2" fill="currentColor"/></symbol>
    <symbol id="i-chev" viewBox="0 0 12 8"><path d="M1 1.5l5 5 5-5" fill="none" stroke="currentColor" stroke-width="1.4"/></symbol>
  </defs>
</svg>

<header class="topbar">
  <div class="brand">LOGO <span>HERE</span></div>
  <div class="top-search">Search here...
    <svg width="16" height="16" viewBox="0 0 16 16"><circle cx="6.5" cy="6.5" r="5.3" fill="none" stroke="#cfd3d7" stroke-width="1.5"/><path d="M10.5 10.5l4.3 4.3" stroke="#cfd3d7" stroke-width="1.6"/></svg>
  </div>
  <svg class="bell" width="15" height="16" viewBox="0 0 15 16"><path d="M7.5 1.5c-2.8 0-4.3 2-4.3 4.6v3.6L1.5 12h12l-1.7-2.3V6.1c0-2.6-1.5-4.6-4.3-4.6zM5.8 13.4a1.7 1.7 0 003.4 0" fill="none" stroke="#9ea4aa" stroke-width="1.2"/></svg>
  <div class="bell-dot">2</div>
  <svg class="gear" width="16" height="16" style="color:#9ea4aa"><use href="#i-gear"/></svg>
  <div class="greeting">Hey, <b>Owen</b></div>
  <div class="avatar" role="img" aria-label="User profile photo"></div>
  <svg class="caret" width="10" height="7" viewBox="0 0 10 7"><path d="M0 0h10L5 6z" fill="#8a9096"/></svg>
</header>

<nav class="mainnav">
  <div class="nav-item" style="top:21px">
    <svg class="ico" width="17" height="17" viewBox="0 0 17 17"><circle cx="8.5" cy="8.5" r="7" fill="none" stroke="#3a4047" stroke-width="1.3"/><path d="M8.5 8.5l3-3M4 8.5h1.5M11.5 8.5H13M8.5 4v1.5" stroke="#3a4047" stroke-width="1.3"/></svg>
    <span class="lbl">Dashboard</span>
    <svg class="chev" width="12" height="8" style="color:#777"><use href="#i-chev"/></svg>
  </div>
  <div class="nav-item nav-active">
    <svg class="ico" width="18" height="17" viewBox="0 0 18 17"><rect x="1" y="1" width="16" height="11" fill="none" stroke="#f7941d" stroke-width="1.3"/><path d="M4 9l3-3 2.5 2L14 4M9 12v3M5 16h8" fill="none" stroke="#f7941d" stroke-width="1.3"/></svg>
    <span class="lbl">Projects</span>
    <svg class="chev" width="12" height="8" style="color:#777;transform:rotate(180deg)"><use href="#i-chev"/></svg>
    <span class="sub">Add New</span>
  </div>
  <div class="nav-item" style="top:143px">
    <svg class="ico" width="18" height="18" viewBox="0 0 18 18"><circle cx="9" cy="3.5" r="2.3" fill="#3a4047"/><path d="M6 9h6M9 6v3M3 11v2M15 11v2M9 9v4" stroke="#3a4047" stroke-width="1.3"/><circle cx="3" cy="14.5" r="1.8" fill="#3a4047"/><circle cx="9" cy="14.5" r="1.8" fill="#3a4047"/><circle cx="15" cy="14.5" r="1.8" fill="#3a4047"/></svg>
    <span class="lbl">Resources</span>
    <svg class="chev" width="12" height="8" style="color:#777"><use href="#i-chev"/></svg>
  </div>
  <div class="nav-item" style="top:192px">
    <svg class="ico" width="19" height="18" viewBox="0 0 19 18"><path d="M1 17h17M2 17V3h2v14M4 17V9l4 3V9l4 3V9l4 3v5" fill="none" stroke="#3a4047" stroke-width="1.3"/></svg>
    <span class="lbl">Plants</span>
    <svg class="chev" width="12" height="8" style="color:#777"><use href="#i-chev"/></svg>
  </div>
  <div class="nav-item" style="top:242px">
    <svg class="ico" width="18" height="18" style="color:#3a4047"><use href="#i-tag-o"/></svg>
    <span class="lbl">Tags</span>
    <svg class="chev" width="12" height="8" style="color:#777"><use href="#i-chev"/></svg>
  </div>
  <div class="nav-item" style="top:291px">
    <svg class="ico" width="17" height="18" viewBox="0 0 17 18"><circle cx="8.5" cy="5" r="4" fill="none" stroke="#3a4047" stroke-width="1.3"/><path d="M1 17c0-4 3.4-6.5 7.5-6.5S16 13 16 17z" fill="none" stroke="#3a4047" stroke-width="1.3"/></svg>
    <span class="lbl">Clients</span>
    <svg class="chev" width="12" height="8" style="color:#777"><use href="#i-chev"/></svg>
  </div>
</nav>

<aside class="subpanel">
  <div class="show">Show</div>
  <div class="sub-item" style="top:54px">
    <svg class="arrow" width="6" height="9" viewBox="0 0 6 9"><path d="M0 0l6 4.5L0 9z" fill="#888"/></svg>
    <svg class="ico" width="18" height="18" viewBox="0 0 18 18"><rect x="1" y="1" width="16" height="11" fill="none" stroke="#3a4047" stroke-width="1.3"/><path d="M4 9l3-3 2.5 2L14 4M9 12v3M5 16h8" fill="none" stroke="#3a4047" stroke-width="1.3"/></svg>
    <span class="lbl">Project List</span><span class="badge" style="background:var(--badge-blue)">67</span>
  </div>
  <div class="sub-item" style="top:94px">
    <svg class="arrow" width="6" height="9" viewBox="0 0 6 9"><path d="M0 0l6 4.5L0 9z" fill="#888"/></svg>
    <svg class="ico" width="18" height="18" viewBox="0 0 18 18"><circle cx="9" cy="3.5" r="2.3" fill="#3a4047"/><path d="M6 9h6M9 6v3M3 11v2M15 11v2M9 9v4" stroke="#3a4047" stroke-width="1.3"/><circle cx="3" cy="14.5" r="1.8" fill="#3a4047"/><circle cx="9" cy="14.5" r="1.8" fill="#3a4047"/><circle cx="15" cy="14.5" r="1.8" fill="#3a4047"/></svg>
    <span class="lbl">Resource</span><span class="badge" style="background:var(--badge-red)">55</span>
  </div>
  <div class="sub-item" style="top:134px">
    <svg class="arrow" width="6" height="9" viewBox="0 0 6 9"><path d="M0 0l6 4.5L0 9z" fill="#888"/></svg>
    <svg class="ico" width="19" height="18" viewBox="0 0 19 18"><path d="M1 17h17M2 17V3h2v14M4 17V9l4 3V9l4 3V9l4 3v5" fill="none" stroke="#3a4047" stroke-width="1.3"/></svg>
    <span class="lbl">Plant</span><span class="badge" style="background:var(--badge-green)">25</span>
  </div>
  <div class="sub-item current" style="top:173px">
    <svg class="arrow" width="9" height="6" viewBox="0 0 9 6" style="top:14px;left:11px"><path d="M0 0h9L4.5 6z" fill="#f7941d"/></svg>
    <svg class="ico" width="18" height="18" style="color:var(--orange)"><use href="#i-tag-o"/></svg>
    <span class="lbl">Project Tags</span><span class="badge" style="background:var(--badge-orange)">115</span>
  </div>
  <div class="tag-search">Search for...</div>
  <div class="group-title" style="top:271px">1.1 Not Working</div>
  <div class="chip" style="top:297px"><svg width="13" height="13" style="color:#3a4047"><use href="#i-tag-o"/></svg>Day Booked Off</div>
  <div class="chip" style="top:326px"><svg width="13" height="13" style="color:#3a4047"><use href="#i-tag-o"/></svg>RDO</div>
  <div class="group-title" style="top:371px">1.0 Trades</div>
  <div class="chip" style="top:398px"><svg width="13" height="13" style="color:#3a4047"><use href="#i-tag-o"/></svg>Lorem ipsum</div>
  <div class="chip" style="top:426px"><svg width="13" height="13" style="color:#3a4047"><use href="#i-tag-o"/></svg>Lorem ipsum</div>
  <div class="chip" style="top:455px"><svg width="13" height="13" style="color:#3a4047"><use href="#i-tag-o"/></svg>Lorem ipsum</div>
  <div class="chip" style="top:483px"><svg width="13" height="13" style="color:#3a4047"><use href="#i-tag-o"/></svg>Lorem ipsum</div>
  <div class="chip" style="top:512px"><svg width="13" height="13" style="color:#3a4047"><use href="#i-tag-o"/></svg>Lorem ipsum</div>
  <div class="chip" style="top:540px"><svg width="13" height="13" style="color:#3a4047"><use href="#i-tag-o"/></svg>Lorem ipsum</div>
  <div class="chip" style="top:569px"><svg width="13" height="13" style="color:#3a4047"><use href="#i-tag-o"/></svg>Lorem ipsum</div>
  <div class="group-title" style="top:612px">2.1 Task - Steel/Shot</div>
</aside>
<div class="scroll-track"></div>
<div class="collapse"><svg width="8" height="11" viewBox="0 0 8 11"><path d="M7 1L2 5.5 7 10" fill="none" stroke="#777" stroke-width="1.5"/></svg></div>

<section class="filter">
  <div class="filter-title">Filter By Date</div>
  <div class="field" style="left:153px;width:134px">10-01-2018
    <svg width="15" height="14" viewBox="0 0 15 14"><rect x=".6" y="1.6" width="13.8" height="11.8" fill="none" stroke="#4fd1b5"/><path d="M.6 4.5h13.8M3 7h2M6.5 7h2M10 7h2M3 10h2M6.5 10h2M10 10h2" stroke="#4fd1b5"/></svg></div>
  <div class="field" style="left:302px;width:140px">10-01-2018
    <svg width="15" height="14" viewBox="0 0 15 14"><rect x=".6" y="1.6" width="13.8" height="11.8" fill="none" stroke="#4fd1b5"/><path d="M.6 4.5h13.8M3 7h2M6.5 7h2M10 7h2M3 10h2M6.5 10h2M10 10h2" stroke="#4fd1b5"/></svg></div>
  <div class="field" style="left:451px;width:116px">Select Project<svg width="10" height="6" viewBox="0 0 10 6" style="top:11px"><path d="M0 0h10L5 6z" fill="#4d5358"/></svg></div>
  <div class="field" style="left:576px;width:116px">Select Client<svg width="10" height="6" viewBox="0 0 10 6" style="top:11px"><path d="M0 0h10L5 6z" fill="#4d5358"/></svg></div>
  <div class="field" style="left:701px;width:116px">Select Tags<svg width="10" height="6" viewBox="0 0 10 6" style="top:11px"><path d="M0 0h10L5 6z" fill="#4d5358"/></svg></div>
  <div class="btn" style="left:153px;width:87px">Yesterday</div>
  <div class="btn" style="left:249px;width:87px">Today</div>
  <div class="btn" style="left:346px;width:87px">Tomorrow</div>
  <div class="btn" style="left:443px;width:87px">Next Week</div>
  <div class="btn apply" style="left:577px;width:115px">Apply Filter</div>
  <div class="btn clear" style="left:701px;width:116px">Clear Filter</div>
</section>

<div class="datebar">
  <svg class="cal" width="17" height="16" viewBox="0 0 17 16"><rect x=".7" y="1.7" width="15.6" height="13.6" fill="none" stroke="#fff" stroke-width="1.2"/><path d="M.7 5h15.6M3.5 8h2M7.5 8h2M11.5 8h2M3.5 11.5h2M7.5 11.5h2M11.5 11.5h2" stroke="#fff" stroke-width="1.2"/></svg>
  <div class="day">09-Jan-2018 [Tuesday]</div>
  <div class="comment">Comment<svg width="10" height="7" style="color:#fff"><use href="#i-chev"/></svg></div>
  <div class="stat" style="left:523px">Projects assigned 15 of 67</div>
  <div class="stat" style="left:687px">Resoures scheduled 50 of 55</div>
</div>

<main class="board">
<!-- block template repeated for 21 project blocks -->
<article class="block"><div class="block-head"><div class="title">21356-Lorem Ipsum-27d</div><div class="addr">WCX-Larkin St. Westvale</div><svg width="8" height="8" style="color:#fff"><use href="#i-gear"/></svg></div><div class="tags"><div class="row trade"><svg width="7" height="7" style="color:#555"><use href="#i-tag"/></svg>Trade: Shotcrete<span class="x">x</span></div><div class="row"><svg width="7" height="7" style="color:#555"><use href="#i-tag"/></svg>Task: Piled Walls<span class="x">x</span></div><div class="row"><svg width="7" height="7" style="color:#555"><use href="#i-tag"/></svg>Start: 6:45am<span class="x">x</span></div><div class="row ok"><svg width="7" height="7" style="color:#555"><use href="#i-tag"/></svg>Confirmed<span class="x">x</span></div></div><div class="crew"><div class="row lead"><svg width="7" height="7" style="color:#555"><use href="#i-tag"/></svg>Danny K<span class="x">x</span></div><div class="row"><svg width="7" height="7" style="color:#555"><use href="#i-tag"/></svg>Marco L<span class="x">x</span></div><div class="row"><svg width="7" height="7" style="color:#555"><use href="#i-tag"/></svg>Sam P<span class="x">x</span></div></div><div class="foot">3 Resources, 0 Plant Assigned</div></article>
<article class="block"><div class="block-head"><div class="title">21356-Lorem Ipsum-27d</div><div class="addr">WCX-Larkin St. Westvale</div><svg width="8" height="8" style="color:#fff"><use href="#i-gear"/></svg></div><div class="tags"><div class="row trade"><svg width="7" height="7" style="color:#555"><use href="#i-tag"/></svg>Trade: Shotcrete<span class="x">x</span></div><div class="row"><svg width="7" height="7" style="color:#555"><use href="#i-tag"/></svg>Task: Piled Walls<span class="x">x</span></div><div class="row"><svg width="7" height="7" style="color:#555"><use href="#i-tag"/></svg>Start: 6:45am<span class="x">x</span></div><div class="row ok"><svg width="7" height="7" style="color:#555"><use href="#i-tag"/></svg>Confirmed<span class="x">x</span></div></div><div class="crew"><div class="row lead"><svg width="7" height="7" style="color:#555"><use href="#i-tag"/></svg>Danny K<span class="x">x</span></div><div class="row"><svg width="7" height="7" style="color:#555"><use href="#i-tag"/></svg>Marco L<span class="x">x</span></div><div class="row"><svg width="7" height="7" style="color:#555"><use href="#i-tag"/></svg>Sam P<span class="x">x</span></div></div><div class="foot">3 Resources, 0 Plant Assigned</div></article>
<article class="block"><div class="block-head"><div class="title">21356-Lorem Ipsum-27d</div><div class="addr">WCX-Larkin St. Westvale</div><svg width="8" height="8" style="color:#fff"><use href="#i-gear"/></svg></div><div class="tags"><div class="row trade"><svg width="7" height="7" style="color:#555"><use href="#i-tag"/></svg>Trade: Shotcrete<span class="x">x</span></div><div class="row"><svg width="7" height="7" style="color:#555"><use href="#i-tag"/></svg>Task: Piled Walls<span class="x">x</span></div><div class="row"><svg width="7" height="7" style="color:#555"><use href="#i-tag"/></svg>Start: 6:45am<span class="x">x</span></div><div class="row ok"><svg width="7" height="7" style="color:#555"><use href="#i-tag"/></svg>Confirmed<span class="x">x</span></div></div><div class="crew"><div class="row lead"><svg width="7" height="7" style="color:#555"><use href="#i-tag"/></svg>Danny K<span class="x">x</span></div><div class="row"><svg width="7" height="7" style="color:#555"><use href="#i-tag"/></svg>Marco L<span class="x">x</span></div><div class="row"><svg width="7" height="7" style="color:#555"><use href="#i-tag"/></svg>Sam P<span class="x">x</span></div></div><div class="foot">3 Resources, 0 Plant Assigned</div></article>
<article class="block"><div class="block-head"><div class="title">21356-Lorem Ipsum-27d</div><div class="addr">WCX-Larkin St. Westvale</div><svg width="8" height="8" style="color:#fff"><use href="#i-gear"/></svg></div><div class="tags"><div class="row trade"><svg width="7" height="7" style="color:#555"><use href="#i-tag"/></svg>Trade: Shotcrete<span class="x">x</span></div><div class="row"><svg width="7" height="7" style="color:#555"><use href="#i-tag"/></svg>Task: Piled Walls<span class="x">x</span></div><div class="row"><svg width="7" height="7" style="color:#555"><use href="#i-tag"/></svg>Start: 6:45am<span class="x">x</span></div><div class="row ok"><svg width="7" height="7" style="color:#555"><use href="#i-tag"/></svg>Confirmed<span class="x">x</span></div></div><div class="crew"><div class="row lead"><svg width="7" height="7" style="color:#555"><use href="#i-tag"/></svg>Danny K<span class="x">x</span></div><div class="row"><svg width="7" height="7" style="color:#555"><use href="#i-tag"/></svg>Marco L<span class="x">x</span></div><div class="row"><svg width="7" height="7" style="color:#555"><use href="#i-tag"/></svg>Sam P<span class="x">x</span></div></div><div class="foot">3 Resources, 0 Plant Assigned</div></article>
<article class="block"><div class="block-head"><div class="title">21356-Lorem Ipsum-27d</div><div class="addr">WCX-Larkin St. Westvale</div><svg width="8" height="8" style="color:#fff"><use href="#i-gear"/></svg></div><div class="tags"><div class="row trade"><svg width="7" height="7" style="color:#555"><use href="#i-tag"/></svg>Trade: Shotcrete<span class="x">x</span></div><div class="row"><svg width="7" height="7" style="color:#555"><use href="#i-tag"/></svg>Task: Piled Walls<span class="x">x</span></div><div class="row"><svg width="7" height="7" style="color:#555"><use href="#i-tag"/></svg>Start: 6:45am<span class="x">x</span></div><div class="row ok"><svg width="7" height="7" style="color:#555"><use href="#i-tag"/></svg>Confirmed<span class="x">x</span></div></div><div class="crew"><div class="row lead"><svg width="7" height="7" style="color:#555"><use href="#i-tag"/></svg>Danny K<span class="x">x</span></div><div class="row"><svg width="7" height="7" style="color:#555"><use href="#i-tag"/></svg>Marco L<span class="x">x</span></div><div class="row"><svg width="7" height="7" style="color:#555"><use href="#i-tag"/></svg>Sam P<span class="x">x</span></div></div><div class="foot">3 Resources, 0 Plant Assigned</div></article>
<article class="block"><div class="block-head"><div class="title">21356-Lorem Ipsum-27d</div><div class="addr">WCX-Larkin St. Westvale</div><svg width="8" height="8" style="color:#fff"><use href="#i-gear"/></svg></div><div class="tags"><div class="row trade"><svg width="7" height="7" style="color:#555"><use href="#i-tag"/></svg>Trade: Shotcrete<span class="x">x</span></div><div class="row"><svg width="7" height="7" style="color:#555"><use href="#i-tag"/></svg>Task: Piled Walls<span class="x">x</span></div><div class="row"><svg width="7" height="7" style="color:#555"><use href="#i-tag"/></svg>Start: 6:45am<span class="x">x</span></div><div class="row ok"><svg width="7" height="7" style="color:#555"><use href="#i-tag"/></svg>Confirmed<span class="x">x</span></div></div><div class="crew"><div class="row lead"><svg width="7" height="7" style="color:#555"><use href="#i-tag"/></svg>Danny K<span class="x">x</span></div><div class="row"><svg width="7" height="7" style="color:#555"><use href="#i-tag"/></svg>Marco L<span class="x">x</span></div><div class="row"><svg width="7" height="7" style="color:#555"><use href="#i-tag"/></svg>Sam P<span class="x">x</span></div></div><div class="foot">3 Resources, 0 Plant Assigned</div></article>
<article class="block"><div class="block-head"><div class="title">21356-Lorem Ipsum-27d</div><div class="addr">WCX-Larkin St. Westvale</div><svg width="8" height="8" style="color:#fff"><use href="#i-gear"/></svg></div><div class="tags"><div class="row trade"><svg width="7" height="7" style="color:#555"><use href="#i-tag"/></svg>Trade: Shotcrete<span class="x">x</span></div><div class="row"><svg width="7" height="7" style="color:#555"><use href="#i-tag"/></svg>Task: Piled Walls<span class="x">x</span></div><div class="row"><svg width="7" height="7" style="color:#555"><use href="#i-tag"/></svg>Start: 6:45am<span class="x">x</span></div><div class="row ok"><svg width="7" height="7" style="color:#555"><use href="#i-tag"/></svg>Confirmed<span class="x">x</span></div></div><div class="crew"><div class="row lead"><svg width="7" height="7" style="color:#555"><use href="#i-tag"/></svg>Danny K<span class="x">x</span></div><div class="row"><svg width="7" height="7" style="color:#555"><use href="#i-tag"/></svg>Marco L<span class="x">x</span></div><div class="row"><svg width="7" height="7" style="color:#555"><use href="#i-tag"/></svg>Sam P<span class="x">x</span></div></div><div class="foot">3 Resources, 0 Plant Assigned</div></article>

<article class="block"><div class="block-head"><div class="title">21356-Lorem Ipsum-27d</div><div class="addr">WCX-Larkin St. Westvale</div><svg width="8" height="8" style="color:#fff"><use href="#i-gear"/></svg></div><div class="tags"><div class="row trade"><svg width="7" height="7" style="color:#555"><use href="#i-tag"/></svg>Trade: Shotcrete<span class="x">x</span></div><div class="row"><svg width="7" height="7" style="color:#555"><use href="#i-tag"/></svg>Task: Piled Walls<span class="x">x</span></div><div class="row"><svg width="7" height="7" style="color:#555"><use href="#i-tag"/></svg>Start: 6:45am<span class="x">x</span></div><div class="row ok"><svg width="7" height="7" style="color:#555"><use href="#i-tag"/></svg>Confirmed<span class="x">x</span></div></div><div class="crew"><div class="row lead"><svg width="7" height="7" style="color:#555"><use href="#i-tag"/></svg>Danny K<span class="x">x</span></div><div class="row"><svg width="7" height="7" style="color:#555"><use href="#i-tag"/></svg>Marco L<span class="x">x</span></div><div class="row"><svg width="7" height="7" style="color:#555"><use href="#i-tag"/></svg>Sam P<span class="x">x</span></div></div><div class="foot">3 Resources, 0 Plant Assigned</div></article>
<article class="block"><div class="block-head"><div class="title">21356-Lorem Ipsum-27d</div><div class="addr">WCX-Larkin St. Westvale</div><svg width="8" height="8" style="color:#fff"><use href="#i-gear"/></svg></div><div class="tags"><div class="row trade"><svg width="7" height="7" style="color:#555"><use href="#i-tag"/></svg>Trade: Shotcrete<span class="x">x</span></div><div class="row"><svg width="7" height="7" style="color:#555"><use href="#i-tag"/></svg>Task: Piled Walls<span class="x">x</span></div><div class="row"><svg width="7" height="7" style="color:#555"><use href="#i-tag"/></svg>Start: 6:45am<span class="x">x</span></div><div class="row ok"><svg width="7" height="7" style="color:#555"><use href="#i-tag"/></svg>Confirmed<span class="x">x</span></div></div><div class="crew"><div class="row lead"><svg width="7" height="7" style="color:#555"><use href="#i-tag"/></svg>Danny K<span class="x">x</span></div><div class="row"><svg width="7" height="7" style="color:#555"><use href="#i-tag"/></svg>Marco L<span class="x">x</span></div><div class="row"><svg width="7" height="7" style="color:#555"><use href="#i-tag"/></svg>Sam P<span class="x">x</span></div></div><div class="foot">3 Resources, 0 Plant Assigned</div></article>
<article class="block"><div class="block-head"><div class="title">21356-Lorem Ipsum-27d</div><div class="addr">WCX-Larkin St. Westvale</div><svg width="8" height="8" style="color:#fff"><use href="#i-gear"/></svg></div><div class="tags"><div class="row trade"><svg width="7" height="7" style="color:#555"><use href="#i-tag"/></svg>Trade: Shotcrete<span class="x">x</span></div><div class="row"><svg width="7" height="7" style="color:#555"><use href="#i-tag"/></svg>Task: Piled Walls<span class="x">x</span></div><div class="row"><svg width="7" height="7" style="color:#555"><use href="#i-tag"/></svg>Start: 6:45am<span class="x">x</span></div><div class="row ok"><svg width="7" height="7" style="color:#555"><use href="#i-tag"/></svg>Confirmed<span class="x">x</span></div></div><div class="crew"><div class="row lead"><svg width="7" height="7" style="color:#555"><use href="#i-tag"/></svg>Danny K<span class="x">x</span></div><div class="row"><svg width="7" height="7" style="color:#555"><use href="#i-tag"/></svg>Marco L<span class="x">x</span></div><div class="row"><svg width="7" height="7" style="color:#555"><use href="#i-tag"/></svg>Sam P<span class="x">x</span></div></div><div class="foot">3 Resources, 0 Plant Assigned</div></article>
<article class="block"><div class="block-head"><div class="title">21356-Lorem Ipsum-27d</div><div class="addr">WCX-Larkin St. Westvale</div><svg width="8" height="8" style="color:#fff"><use href="#i-gear"/></svg></div><div class="tags"><div class="row trade"><svg width="7" height="7" style="color:#555"><use href="#i-tag"/></svg>Trade: Shotcrete<span class="x">x</span></div><div class="row"><svg width="7" height="7" style="color:#555"><use href="#i-tag"/></svg>Task: Piled Walls<span class="x">x</span></div><div class="row"><svg width="7" height="7" style="color:#555"><use href="#i-tag"/></svg>Start: 6:45am<span class="x">x</span></div><div class="row ok"><svg width="7" height="7" style="color:#555"><use href="#i-tag"/></svg>Confirmed<span class="x">x</span></div></div><div class="crew"><div class="row lead"><svg width="7" height="7" style="color:#555"><use href="#i-tag"/></svg>Danny K<span class="x">x</span></div><div class="row"><svg width="7" height="7" style="color:#555"><use href="#i-tag"/></svg>Marco L<span class="x">x</span></div><div class="row"><svg width="7" height="7" style="color:#555"><use href="#i-tag"/></svg>Sam P<span class="x">x</span></div></div><div class="foot">3 Resources, 0 Plant Assigned</div></article>
<article class="block"><div class="block-head"><div class="title">21356-Lorem Ipsum-27d</div><div class="addr">WCX-Larkin St. Westvale</div><svg width="8" height="8" style="color:#fff"><use href="#i-gear"/></svg></div><div class="tags"><div class="row trade"><svg width="7" height="7" style="color:#555"><use href="#i-tag"/></svg>Trade: Shotcrete<span class="x">x</span></div><div class="row"><svg width="7" height="7" style="color:#555"><use href="#i-tag"/></svg>Task: Piled Walls<span class="x">x</span></div><div class="row"><svg width="7" height="7" style="color:#555"><use href="#i-tag"/></svg>Start: 6:45am<span class="x">x</span></div><div class="row ok"><svg width="7" height="7" style="color:#555"><use href="#i-tag"/></svg>Confirmed<span class="x">x</span></div></div><div class="crew"><div class="row lead"><svg width="7" height="7" style="color:#555"><use href="#i-tag"/></svg>Danny K<span class="x">x</span></div><div class="row"><svg width="7" height="7" style="color:#555"><use href="#i-tag"/></svg>Marco L<span class="x">x</span></div><div class="row"><svg width="7" height="7" style="color:#555"><use href="#i-tag"/></svg>Sam P<span class="x">x</span></div></div><div class="foot">3 Resources, 0 Plant Assigned</div></article>
<article class="block"><div class="block-head"><div class="title">21356-Lorem Ipsum-27d</div><div class="addr">WCX-Larkin St. Westvale</div><svg width="8" height="8" style="color:#fff"><use href="#i-gear"/></svg></div><div class="tags"><div class="row trade"><svg width="7" height="7" style="color:#555"><use href="#i-tag"/></svg>Trade: Shotcrete<span class="x">x</span></div><div class="row"><svg width="7" height="7" style="color:#555"><use href="#i-tag"/></svg>Task: Piled Walls<span class="x">x</span></div><div class="row"><svg width="7" height="7" style="color:#555"><use href="#i-tag"/></svg>Start: 6:45am<span class="x">x</span></div><div class="row ok"><svg width="7" height="7" style="color:#555"><use href="#i-tag"/></svg>Confirmed<span class="x">x</span></div></div><div class="crew"><div class="row lead"><svg width="7" height="7" style="color:#555"><use href="#i-tag"/></svg>Danny K<span class="x">x</span></div><div class="row"><svg width="7" height="7" style="color:#555"><use href="#i-tag"/></svg>Marco L<span class="x">x</span></div><div class="row"><svg width="7" height="7" style="color:#555"><use href="#i-tag"/></svg>Sam P<span class="x">x</span></div></div><div class="foot">3 Resources, 0 Plant Assigned</div></article>
<article class="block"><div class="block-head"><div class="title">21356-Lorem Ipsum-27d</div><div class="addr">WCX-Larkin St. Westvale</div><svg width="8" height="8" style="color:#fff"><use href="#i-gear"/></svg></div><div class="tags"><div class="row trade"><svg width="7" height="7" style="color:#555"><use href="#i-tag"/></svg>Trade: Shotcrete<span class="x">x</span></div><div class="row"><svg width="7" height="7" style="color:#555"><use href="#i-tag"/></svg>Task: Piled Walls<span class="x">x</span></div><div class="row"><svg width="7" height="7" style="color:#555"><use href="#i-tag"/></svg>Start: 6:45am<span class="x">x</span></div><div class="row ok"><svg width="7" height="7" style="color:#555"><use href="#i-tag"/></svg>Confirmed<span class="x">x</span></div></div><div class="crew"><div class="row lead"><svg width="7" height="7" style="color:#555"><use href="#i-tag"/></svg>Danny K<span class="x">x</span></div><div class="row"><svg width="7" height="7" style="color:#555"><use href="#i-tag"/></svg>Marco L<span class="x">x</span></div><div class="row"><svg width="7" height="7" style="color:#555"><use href="#i-tag"/></svg>Sam P<span class="x">x</span></div></div><div class="foot">3 Resources, 0 Plant Assigned</div></article>

<article class="block"><div class="block-head"><div class="title">21356-Lorem Ipsum-27d</div><div class="addr">WCX-Larkin St. Westvale</div><svg width="8" height="8" style="color:#fff"><use href="#i-gear"/></svg></div><div class="tags"><div class="row trade"><svg width="7" height="7" style="color:#555"><use href="#i-tag"/></svg>Trade: Shotcrete<span class="x">x</span></div><div class="row"><svg width="7" height="7" style="color:#555"><use href="#i-tag"/></svg>Task: Piled Walls<span class="x">x</span></div><div class="row"><svg width="7" height="7" style="color:#555"><use href="#i-tag"/></svg>Start: 6:45am<span class="x">x</span></div><div class="row ok"><svg width="7" height="7" style="color:#555"><use href="#i-tag"/></svg>Confirmed<span class="x">x</span></div></div><div class="crew"><div class="row lead"><svg width="7" height="7" style="color:#555"><use href="#i-tag"/></svg>Danny K<span class="x">x</span></div><div class="row"><svg width="7" height="7" style="color:#555"><use href="#i-tag"/></svg>Marco L<span class="x">x</span></div><div class="row"><svg width="7" height="7" style="color:#555"><use href="#i-tag"/></svg>Sam P<span class="x">x</span></div></div><div class="foot">3 Resources, 0 Plant Assigned</div></article>
<article class="block"><div class="block-head"><div class="title">21356-Lorem Ipsum-27d</div><div class="addr">WCX-Larkin St. Westvale</div><svg width="8" height="8" style="color:#fff"><use href="#i-gear"/></svg></div><div class="tags"><div class="row trade"><svg width="7" height="7" style="color:#555"><use href="#i-tag"/></svg>Trade: Shotcrete<span class="x">x</span></div><div class="row"><svg width="7" height="7" style="color:#555"><use href="#i-tag"/></svg>Task: Piled Walls<span class="x">x</span></div><div class="row"><svg width="7" height="7" style="color:#555"><use href="#i-tag"/></svg>Start: 6:45am<span class="x">x</span></div><div class="row ok"><svg width="7" height="7" style="color:#555"><use href="#i-tag"/></svg>Confirmed<span class="x">x</span></div></div><div class="crew"><div class="row lead"><svg width="7" height="7" style="color:#555"><use href="#i-tag"/></svg>Danny K<span class="x">x</span></div><div class="row"><svg width="7" height="7" style="color:#555"><use href="#i-tag"/></svg>Marco L<span class="x">x</span></div><div class="row"><svg width="7" height="7" style="color:#555"><use href="#i-tag"/></svg>Sam P<span class="x">x</span></div></div><div class="foot">3 Resources, 0 Plant Assigned</div></article>
<article class="block"><div class="block-head"><div class="title">21356-Lorem Ipsum-27d</div><div class="addr">WCX-Larkin St. Westvale</div><svg width="8" height="8" style="color:#fff"><use href="#i-gear"/></svg></div><div class="tags"><div class="row trade"><svg width="7" height="7" style="color:#555"><use href="#i-tag"/></svg>Trade: Shotcrete<span class="x">x</span></div><div class="row"><svg width="7" height="7" style="color:#555"><use href="#i-tag"/></svg>Task: Piled Walls<span class="x">x</span></div><div class="row"><svg width="7" height="7" style="color:#555"><use href="#i-tag"/></svg>Start: 6:45am<span class="x">x</span></div><div class="row ok"><svg width="7" height="7" style="color:#555"><use href="#i-tag"/></svg>Confirmed<span class="x">x</span></div></div><div class="crew"><div class="row lead"><svg width="7" height="7" style="color:#555"><use href="#i-tag"/></svg>Danny K<span class="x">x</span></div><div class="row"><svg width="7" height="7" style="color:#555"><use href="#i-tag"/></svg>Marco L<span class="x">x</span></div><div class="row"><svg width="7" height="7" style="color:#555"><use href="#i-tag"/></svg>Sam P<span class="x">x</span></div></div><div class="foot">3 Resources, 0 Plant Assigned</div></article>
<article class="block"><div class="block-head"><div class="title">21356-Lorem Ipsum-27d</div><div class="addr">WCX-Larkin St. Westvale</div><svg width="8" height="8" style="color:#fff"><use href="#i-gear"/></svg></div><div class="tags"><div class="row trade"><svg width="7" height="7" style="color:#555"><use href="#i-tag"/></svg>Trade: Shotcrete<span class="x">x</span></div><div class="row"><svg width="7" height="7" style="color:#555"><use href="#i-tag"/></svg>Task: Piled Walls<span class="x">x</span></div><div class="row"><svg width="7" height="7" style="color:#555"><use href="#i-tag"/></svg>Start: 6:45am<span class="x">x</span></div><div class="row ok"><svg width="7" height="7" style="color:#555"><use href="#i-tag"/></svg>Confirmed<span class="x">x</span></div></div><div class="crew"><div class="row lead"><svg width="7" height="7" style="color:#555"><use href="#i-tag"/></svg>Danny K<span class="x">x</span></div><div class="row"><svg width="7" height="7" style="color:#555"><use href="#i-tag"/></svg>Marco L<span class="x">x</span></div><div class="row"><svg width="7" height="7" style="color:#555"><use href="#i-tag"/></svg>Sam P<span class="x">x</span></div></div><div class="foot">3 Resources, 0 Plant Assigned</div></article>
<article class="block"><div class="block-head"><div class="title">21356-Lorem Ipsum-27d</div><div class="addr">WCX-Larkin St. Westvale</div><svg width="8" height="8" style="color:#fff"><use href="#i-gear"/></svg></div><div class="tags"><div class="row trade"><svg width="7" height="7" style="color:#555"><use href="#i-tag"/></svg>Trade: Shotcrete<span class="x">x</span></div><div class="row"><svg width="7" height="7" style="color:#555"><use href="#i-tag"/></svg>Task: Piled Walls<span class="x">x</span></div><div class="row"><svg width="7" height="7" style="color:#555"><use href="#i-tag"/></svg>Start: 6:45am<span class="x">x</span></div><div class="row ok"><svg width="7" height="7" style="color:#555"><use href="#i-tag"/></svg>Confirmed<span class="x">x</span></div></div><div class="crew"><div class="row lead"><svg width="7" height="7" style="color:#555"><use href="#i-tag"/></svg>Danny K<span class="x">x</span></div><div class="row"><svg width="7" height="7" style="color:#555"><use href="#i-tag"/></svg>Marco L<span class="x">x</span></div><div class="row"><svg width="7" height="7" style="color:#555"><use href="#i-tag"/></svg>Sam P<span class="x">x</span></div></div><div class="foot">3 Resources, 0 Plant Assigned</div></article>
<article class="block"><div class="block-head"><div class="title">21356-Lorem Ipsum-27d</div><div class="addr">WCX-Larkin St. Westvale</div><svg width="8" height="8" style="color:#fff"><use href="#i-gear"/></svg></div><div class="tags"><div class="row trade"><svg width="7" height="7" style="color:#555"><use href="#i-tag"/></svg>Trade: Shotcrete<span class="x">x</span></div><div class="row"><svg width="7" height="7" style="color:#555"><use href="#i-tag"/></svg>Task: Piled Walls<span class="x">x</span></div><div class="row"><svg width="7" height="7" style="color:#555"><use href="#i-tag"/></svg>Start: 6:45am<span class="x">x</span></div><div class="row ok"><svg width="7" height="7" style="color:#555"><use href="#i-tag"/></svg>Confirmed<span class="x">x</span></div></div><div class="crew"><div class="row lead"><svg width="7" height="7" style="color:#555"><use href="#i-tag"/></svg>Danny K<span class="x">x</span></div><div class="row"><svg width="7" height="7" style="color:#555"><use href="#i-tag"/></svg>Marco L<span class="x">x</span></div><div class="row"><svg width="7" height="7" style="color:#555"><use href="#i-tag"/></svg>Sam P<span class="x">x</span></div></div><div class="foot">3 Resources, 0 Plant Assigned</div></article>
<article class="block"><div class="block-head"><div class="title">21356-Lorem Ipsum-27d</div><div class="addr">WCX-Larkin St. Westvale</div><svg width="8" height="8" style="color:#fff"><use href="#i-gear"/></svg></div><div class="tags"><div class="row trade"><svg width="7" height="7" style="color:#555"><use href="#i-tag"/></svg>Trade: Shotcrete<span class="x">x</span></div><div class="row"><svg width="7" height="7" style="color:#555"><use href="#i-tag"/></svg>Task: Piled Walls<span class="x">x</span></div><div class="row"><svg width="7" height="7" style="color:#555"><use href="#i-tag"/></svg>Start: 6:45am<span class="x">x</span></div><div class="row ok"><svg width="7" height="7" style="color:#555"><use href="#i-tag"/></svg>Confirmed<span class="x">x</span></div></div><div class="crew"><div class="row lead"><svg width="7" height="7" style="color:#555"><use href="#i-tag"/></svg>Danny K<span class="x">x</span></div><div class="row"><svg width="7" height="7" style="color:#555"><use href="#i-tag"/></svg>Marco L<span class="x">x</span></div><div class="row"><svg width="7" height="7" style="color:#555"><use href="#i-tag"/></svg>Sam P<span class="x">x</span></div></div><div class="foot">3 Resources, 0 Plant Assigned</div></article>
</main>
</body>
</html>
```